Mobile Freezer Rental Vehicle Wrap Design

The size dimensions for our mobile freezer unit is:
Side Panels – Widith 141 ¾” X 87” High
Front and Back Panels – Width 71 ¼” X 87” High

Project Overview:
Red Fern Commercial Services is seeking a creative and experienced design firm to develop a compelling and impactful vehicle wrap for our mobile freezer unit. This unit provides emergency freezer rental services to businesses, primarily restaurants, experiencing freezer breakdowns.

Key Objectives:
• Brand Visibility: Enhance brand recognition and visibility for Red Fern Commercial Services.
• Communicate Service: Clearly convey the purpose of the mobile freezer unit: emergency freezer rental solutions.
• Professional Image: Project a professional and reliable image that inspires confidence in our services.
• Visually Appealing: Create a visually engaging and memorable design that stands out on the road.

Design Requirements:
• Incorporate Existing Logo: Seamlessly integrate the existing Red Fern Commercial Services logo into the design.
• "Frozen" Theme:
• Utilize a cool color palette (blues, grays, whites, silvers) to evoke a sense of cold.
• Consider subtle, clean ice or snowflake graphics around the edges to reinforce the cooling concept.
• The overall design should have a "frozen" or "chilled" aesthetic.
• Clear Messaging:
• Include key contact information (phone number, website).
• Consider incorporating short, impactful taglines (e.g., "Emergency Freezer Rentals," "Keeping Your Business Cold," "Fast, Reliable, Cold Storage").
• High-Quality Graphics: Ensure all graphics are high-resolution and suitable for large-format printing.
• Durability: Design should be durable and withstand the elements (sun, rain, etc.). This design will be used to produce a vehicle/auto wrap for the four sides of a mobile freezer (see included pictures).

Target Audience:
• Restaurant owners and managers
• Food service industry professionals
• Businesses that rely on cold storage

Budget:
• Please provide a cost estimate for your design services.

Submission Requirements:
• Please submit 3-5 initial design concepts.
• Include a brief project plan and timeline.
• Provide information about your experience in vehicle wrap design and large-format printing.

Target Market(s)

• Restaurant owners and managers • Food service industry professionals • Businesses that rely on cold storage

Industry/Entity Type

Restaurant Equipment Repair & Maintenance

Other font styles liked:
• Calibri

Colors
0054AA
0677BA
7BADD7
CADEEF
E8F1F8
0094D4
00A9DD
6FCCEA
C7EBF8
E9F6FB
59FF00
82FF00
B8FF75
E3FFCB
F4FFEA
EB3D1F
EC4F4E
F09395
F8D3D4
FCEDEE

Requirements
Must have
• Incorporate existing logo into overall theme placed prominently at the top or center of the design, must have our phone number of 406-872-5094, our company web site address - www.redferncomserv.example
Nice to have
• Tag lines such as "Emergency Mobile Freezer Rental", "Keep Your Products Safe and Frozen!"

```html
<!DOCTYPE html>
<html lang="en">
<head>
<meta charset="utf-8">
<title>Red Fern Commercial Services – Mobile Cold Storage Wrap</title>
<link rel="stylesheet" href="https://fonts.googleapis.com/css2?family=Open+Sans:wght@600;700;800&display=swap">
<style>
  :root {
    --navy: #0a5a94;
    --brand-blue: #0677ba;
    --sky: #0094d4;
    --link-blue: #3a9fd6;
    --ice-deep: #3f9fe2;
    --ice-mid: #7bbfee;
    --ice-light: #c7e6f8;
    --frost: #e9f6fb;
    --panel-white: #f4f6f8;
    --page: #e6eaee;
    --white: #ffffff;
  }
  * { margin: 0; padding: 0; box-sizing: border-box; }
  html, body { width: 1200px; height: 2457px; overflow: hidden; }
  body {
    background: var(--page);
    font-family: "Open Sans", Calibri, sans-serif;
    position: relative;
  }
  .panel {
    position: absolute;
    background: var(--panel-white);
    overflow: hidden;
    box-shadow: 0 2px 8px rgba(0,0,0,.12);
  }
  .panel--side-left { left: 148px; top: 106px; width: 939px; height: 642px; }
  .panel--side-right { left: 112px; top: 924px; width: 941px; height: 642px; }
  .panel--back { left: 47px; top: 1711px; width: 508px; height: 639px; }
  .panel--front { left: 648px; top: 1711px; width: 508px; height: 639px; }

  .ice-art {
    position: absolute; inset: 0;
    background:
      radial-gradient(ellipse at 30% 90%, var(--ice-light) 0%, transparent 45%),
      radial-gradient(ellipse at 80% 10%, var(--ice-light) 0%, transparent 40%),
      linear-gradient(160deg, var(--ice-mid) 0%, var(--ice-deep) 50%, var(--ice-mid) 100%);
  }
  .panel--side-left .ice-art { clip-path: polygon(56% 0, 100% 0, 100% 100%, 27% 100%); }
  .panel--side-right .ice-art { clip-path: polygon(0 0, 46% 0, 68% 100%, 0 100%); }
  .frost-band {
    position: absolute; left: 0; right: 0; top: 130px; height: 215px;
    background: linear-gradient(180deg, transparent 0%, var(--frost) 18%, var(--white) 50%, var(--frost) 82%, transparent 100%);
  }

  .brand-name {
    position: absolute;
    color: var(--brand-blue);
    font-weight: 800;
    line-height: 1;
    text-transform: uppercase;
    white-space: nowrap;
  }
  .brand-name__main { display: block; letter-spacing: 1px; }
  .brand-name__sub { display: block; letter-spacing: 1px; margin-top: 6px; }

  .badge {
    position: absolute;
    background: var(--navy);
    color: var(--white);
    border-radius: 12px;
    text-align: center;
    display: flex; flex-direction: column; justify-content: center;
    border: 2px solid var(--white);
    white-space: nowrap;
  }
  .badge__title { font-weight: 700; line-height: 1.1; }
  .badge__sub { font-weight: 600; line-height: 1.2; }

  .contact { position: absolute; text-align: left; white-space: nowrap; }
  .contact__phone {
    color: var(--navy); font-weight: 700; line-height: 1;
    display: flex; align-items: center; gap: 8px;
  }
  .contact__phone svg { fill: var(--navy); }
  .contact__web { color: var(--link-blue); font-weight: 600; margin-top: 12px; line-height: 1; }

  .headline {
    position: absolute;
    text-align: center;
    color: var(--sky);
    font-weight: 600;
    line-height: 1.18;
    text-transform: uppercase;
    -webkit-text-stroke: 1px var(--navy);
    text-shadow: 0 2px 3px rgba(255,255,255,.7);
    white-space: nowrap;
  }
</style>
</head>
<body>

<section class="panel panel--side-left">
  <div class="ice-art" role="img" aria-label="Ice cubes and cracked ice illustration"></div>
  <div class="brand-name" style="left:30px; top:78px;">
    <span class="brand-name__main" style="font-size:64px;">Red Fern</span>
    <span class="brand-name__sub" style="font-size:25px;">Commercial Services</span>
  </div>
  <div class="badge" style="left:15px; top:270px; width:302px; height:83px;">
    <span class="badge__title" style="font-size:35px;">FOOD SERVICE</span>
    <span class="badge__sub" style="font-size:19px;">INDUSTRY PROFESSIONALS</span>
  </div>
  <div class="contact" style="left:26px; top:420px;">
    <div class="contact__phone" style="font-size:38px;">
      <svg width="32" height="32" viewBox="0 0 24 24"><path d="M6.6 10.8a15.1 15.1 0 0 0 6.6 6.6l2.2-2.2a1 1 0 0 1 1-.25 11.4 11.4 0 0 0 3.6.57 1 1 0 0 1 1 1V20a1 1 0 0 1-1 1A17 17 0 0 1 3 4a1 1 0 0 1 1-1h3.5a1 1 0 0 1 1 1c0 1.25.2 2.45.57 3.57a1 1 0 0 1-.25 1z"/></svg>
      406-872-5094
    </div>
    <div class="contact__web" style="font-size:22px;">REDFERNCOMSERV.EXAMPLE</div>
  </div>
  <div class="headline" style="left:420px; width:500px; top:252px; font-size:58px;">Mobile Cold<br>Storage Rental</div>
</section>

<section class="panel panel--side-right">
  <div class="ice-art" role="img" aria-label="Ice cubes and cracked ice illustration"></div>
  <div class="brand-name" style="left:521px; top:78px;">
    <span class="brand-name__main" style="font-size:64px;">Red Fern</span>
    <span class="brand-name__sub" style="font-size:25px;">Commercial Services</span>
  </div>
  <div class="badge" style="left:623px; top:272px; width:302px; height:83px;">
    <span class="badge__title" style="font-size:35px;">FOOD SERVICE</span>
    <span class="badge__sub" style="font-size:19px;">INDUSTRY PROFESSIONALS</span>
  </div>
  <div class="contact" style="left:600px; top:420px;">
    <div class="contact__phone" style="font-size:38px;">
      <svg width="32" height="32" viewBox="0 0 24 24"><path d="M6.6 10.8a15.1 15.1 0 0 0 6.6 6.6l2.2-2.2a1 1 0 0 1 1-.25 11.4 11.4 0 0 0 3.6.57 1 1 0 0 1 1 1V20a1 1 0 0 1-1 1A17 17 0 0 1 3 4a1 1 0 0 1 1-1h3.5a1 1 0 0 1 1 1c0 1.25.2 2.45.57 3.57a1 1 0 0 1-.25 1z"/></svg>
      406-872-5094
    </div>
    <div class="contact__web" style="font-size:22px;">REDFERNCOMSERV.EXAMPLE</div>
  </div>
  <div class="headline" style="left:10px; width:520px; top:252px; font-size:58px;">Mobile Cold<br>Storage Rental</div>
</section>

<section class="panel panel--back">
  <div class="ice-art" role="img" aria-label="Ice cubes and cracked ice illustration"></div>
  <div class="brand-name" style="left:255px; top:59px;">
    <span class="brand-name__main" style="font-size:40px;">Red Fern</span>
    <span class="brand-name__sub" style="font-size:15px;">Commercial Services</span>
  </div>
  <div class="badge" style="left:223px; top:216px; width:271px; height:73px;">
    <span class="badge__title" style="font-size:30px;">FOOD SERVICE</span>
    <span class="badge__sub" style="font-size:16px;">INDUSTRY PROFESSIONALS</span>
  </div>
  <div class="headline" style="left:208px; width:300px; top:326px; font-size:30px;">Mobile Cold<br>Storage Rental</div>
  <div class="contact" style="left:224px; top:434px;">
    <div class="contact__phone" style="font-size:32px;">
      <svg width="28" height="28" viewBox="0 0 24 24"><path d="M6.6 10.8a15.1 15.1 0 0 0 6.6 6.6l2.2-2.2a1 1 0 0 1 1-.25 11.4 11.4 0 0 0 3.6.57 1 1 0 0 1 1 1V20a1 1 0 0 1-1 1A17 17 0 0 1 3 4a1 1 0 0 1 1-1h3.5a1 1 0 0 1 1 1c0 1.25.2 2.45.57 3.57a1 1 0 0 1-.25 1z"/></svg>
      406-872-5094
    </div>
    <div class="contact__web" style="font-size:17px;">REDFERNCOMSERV.EXAMPLE</div>
  </div>
</section>

<section class="panel panel--front">
  <div class="ice-art" role="img" aria-label="Ice cubes and cracked ice illustration"></div>
  <div class="frost-band"></div>
  <div class="brand-name" style="left:70px; top:171px;">
    <span class="brand-name__main" style="font-size:62px;">Red Fern</span>
    <span class="brand-name__sub" style="font-size:24px;">Commercial Services</span>
  </div>
  <div class="badge" style="left:151px; top:348px; width:218px; height:60px;">
    <span class="badge__title" style="font-size:25px;">FOOD SERVICE</span>
    <span class="badge__sub" style="font-size:13px;">INDUSTRY PROFESSIONALS</span>
  </div>
  <div class="contact" style="left:158px; top:438px;">
    <div class="contact__phone" style="font-size:27px;">
      <svg width="24" height="24" viewBox="0 0 24 24"><path d="M6.6 10.8a15.1 15.1 0 0 0 6.6 6.6l2.2-2.2a1 1 0 0 1 1-.25 11.4 11.4 0 0 0 3.6.57 1 1 0 0 1 1 1V20a1 1 0 0 1-1 1A17 17 0 0 1 3 4a1 1 0 0 1 1-1h3.5a1 1 0 0 1 1 1c0 1.25.2 2.45.57 3.57a1 1 0 0 1-.25 1z"/></svg>
      406-872-5094
    </div>
    <div class="contact__web" style="font-size:16px; margin-top:9px;">REDFERNCOMSERV.EXAMPLE</div>
  </div>
</section>

</body>
</html>
```